Kestrel Ark AI Power Point Pitch Deck Design

We are in need of building out a designed version of the attached Power Point. We are a SaaS company focused on utilizing AI to perform marketing functions for small to medium sized businesses. We are looking for a modern SaaS design for this pitch deck.

I have included a mock up of a design for our logo we are thinking of using, we may change the colors but let's go forward with this scheme as shown. We are looking for a matured design here so on places where we use statistics ways to make the statistics pop graphically. Interesting ways to display the information from slide to slide so it doesn't feel repetitive.

Generally speaking this should feel polished enough for us to go to VC firms to raise money. Happy to answer additional questions.

Target Market(s)

VC's

Industry/Entity Type

SaaS

Font styles to use
Sans Serif

Requirements
Must have
• A complete design that feels branded to an AI SaaS
Nice to have
• I'd like graphics within the deck that highlight various statistics
Should not have
• Should not feel cartoon like. It should be professional and modern

```html
<!DOCTYPE html>
<html lang="en">
<head>
<meta charset="utf-8">
<title>The Current B2B SMB Landscape</title>
<link href="https://fonts.googleapis.com/css2?family=Lato:wght@400;700&display=swap" rel="stylesheet">
<style>
  :root {
    --bg: #326489;
    --chevron-light: #3a7a9f;
    --chevron-mid: #2d5b80;
    --chevron-dark: #22476a;
    --card: #ffffff;
    --tab: #2f6489;
    --tab-light: #3b779c;
    --ink: #1f1f1f;
    --white: #ffffff;
  }
  * { margin: 0; padding: 0; box-sizing: border-box; }
  html, body { width: 1200px; height: 675px; overflow: hidden; }
  body { font-family: "Lato", sans-serif; background: var(--bg); }
  .slide { position: relative; width: 1200px; height: 675px; overflow: hidden; background: var(--bg); }
  .decor { position: absolute; inset: 0; }
  .title {
    position: absolute; left: 247px; top: 82px;
    color: var(--white); font-weight: 700; font-size: 37px; letter-spacing: 0.2px;
  }
  .card {
    position: absolute; left: 246px; width: 611px; height: 121px;
    background: var(--card); border-radius: 18px;
    box-shadow: 0 4px 6px rgba(0,0,0,0.25);
  }
  .card-1 { top: 174px; }
  .card-2 { top: 326px; }
  .card-3 { top: 478px; }
  .tab {
    position: absolute; left: 35px; top: -6px; width: 78px; height: 86px;
    background: linear-gradient(180deg, var(--tab), var(--tab-light));
    border-radius: 0 0 39px 39px;
    box-shadow: 0 5px 5px rgba(0,0,0,0.18);
    color: var(--white); font-size: 44px; font-weight: 400;
    display: flex; align-items: center; justify-content: center; padding-bottom: 8px;
  }
  .tab::before {
    content: ""; position: absolute; top: 0; left: 0; right: 0; height: 4px;
    background: rgba(255,255,255,0.35);
  }
  .dot {
    position: absolute; right: 13px; top: 11px; width: 22px; height: 22px;
    border-radius: 50%; background: var(--tab);
  }
  .card-heading { position: absolute; left: 138px; top: 12px; color: var(--ink); font-weight: 400; font-size: 26px; }
  .card-3 .card-heading { font-size: 21px; top: 16px; left: 141px; }
  .card-text { position: absolute; left: 136px; top: 50px; width: 420px; color: var(--ink); font-size: 15px; line-height: 19px; }
  .card-2 .card-heading, .card-2 .card-text { left: 141px; }
  .card-2 .card-text { top: 57px; }
  .card-3 .card-text { left: 141px; top: 50px; }
</style>
</head>
<body>
<main class="slide">
  <svg class="decor" width="1200" height="675" viewBox="0 0 1200 675" aria-hidden="true">
    <polygon points="0,0 90,0 188,100 90,200 0,290" fill="var(--chevron-dark)"/>
    <polygon points="0,0 57,0 155,100 57,200 0,257" fill="var(--chevron-mid)"/>
    <polygon points="0,0 25,0 123,100 25,200 0,225" fill="var(--bg)"/>
    <polygon points="0,10 90,100 0,190" fill="var(--chevron-light)"/>
    <polygon points="875,675 1200,350 1200,420 945,675" fill="var(--chevron-light)"/>
    <polygon points="985,675 1200,460 1200,675" fill="var(--chevron-mid)"/>
    <polygon points="1045,675 1200,520 1200,675" fill="var(--chevron-dark)"/>
  </svg>

  <h1 class="title">THE CURRENT B2B SMB LANDSCAPE</h1>

  <section class="card card-1">
    <div class="tab">A</div>
    <span class="dot"></span>
    <h2 class="card-heading">3.9 MILLION SMBS</h2>
    <p class="card-text">There are 3.9 million small and medium-sized businesses in the United States.</p>
  </section>

  <section class="card card-2">
    <div class="tab">B</div>
    <span class="dot"></span>
    <h2 class="card-heading">CHALLENGES IN GROWTH</h2>
    <p class="card-text">Many of these businesses are striving to grow and compete against massive competitors</p>
  </section>

  <section class="card card-3">
    <div class="tab">C</div>
    <span class="dot"></span>
    <h2 class="card-heading">THE DIGITAL MARKETING DISADVANTAGE</h2>
    <p class="card-text">Digital marketing is tasked with leading their growth efforts, but SMBs are at a distinct disadvantage due to limited re-sources and expertise.</p>
  </section>
</main>
</body>
</html>
```